Tressvane hair oil bottle & packaging (Instagrammable)

I'm a blogger/social media influencer and I'm launching my own hair oil that I created myself. The hair oil is something I've used fora a long time and it makes your hair grow like there's no tomorrow!

I'm looking for a feminine and minimalistic bottle for the hair oil and also a nice packaging for the bottle. Please have a look at my Instagram account (@minaveltroo), I'd love if the product design and color scheme would be inspired by my Instagram feed. I'm looking for a design that would look very 'Instagrammable'

Product name: Tressvane
Bottle size: 100ml

Thank you xx

Target Market(s)

Females

Requirements
Must have
• According to the law this has to be marked on the packaging and on the bottle:
• Amount: 100ml
• Marked on the packaging:
• Ingredients: Burdock root oil, Grapeseed oil, Organic castor oil (maybe somehow draw attention to the fact that it's organic when designing the bottle & packaging), peppermint oil, Lavender oil, Cedarwood oil, Rosemary oil
Nice to have
• I added some photos of Ai Wenna packaging - I absolutely love it! The colour is exactly what I have in mind (also if you check my Instagram it's kind of my 'feed colour' - I'd be happy if the packaging would look something like that. The Ai Wenna packaging is exactly what I meant by 'Instagrammable'.
• Also - if we go for something like this, we could write Glow up! on the inside (so you see that when opening the packaging) or feel free to come up with something yourself, just bear in mind it's a hair oil that promotes hair growth

```html
<!DOCTYPE html>
<html lang="en">
<head>
<meta charset="utf-8">
<title>Tressvane Organic Hair Oil Label</title>
<link rel="stylesheet" href="https://fonts.googleapis.com/css2?family=Quicksand:wght@400;500&display=swap">
<style>
  :root {
    --rust: #963a00;
    --paper: #ffffff;
  }
  html, body {
    margin: 0;
    padding: 0;
    width: 1200px;
    height: 782px;
    overflow: hidden;
    background: var(--paper);
  }
  .label {
    position: relative;
    width: 1200px;
    height: 782px;
    background: var(--paper);
    font-family: "Quicksand", sans-serif;
  }
  .brand-band {
    position: absolute;
    left: 0;
    top: 231px;
    width: 1200px;
    height: 149px;
    background: var(--rust);
    display: flex;
    align-items: center;
    justify-content: center;
  }
  .brand-name {
    margin: 0;
    color: var(--paper);
    font-weight: 400;
    font-size: 78px;
    letter-spacing: 0.62em;
    padding-left: 0.62em;
    text-transform: uppercase;
    line-height: 1;
  }
  .product-info {
    position: absolute;
    left: 0;
    top: 478px;
    width: 1200px;
    text-align: center;
    color: var(--rust);
    text-transform: uppercase;
  }
  .product-type {
    margin: 0;
    font-weight: 400;
    font-size: 46px;
    letter-spacing: 0.48em;
    padding-left: 0.48em;
    line-height: 1.1;
  }
  .product-volume {
    margin: 0;
    font-weight: 400;
    font-size: 42px;
    letter-spacing: 0.5em;
    padding-left: 0.5em;
    line-height: 1.15;
  }
</style>
</head>
<body>
  <main class="label">
    <div class="brand-band">
      <h1 class="brand-name">Tressvane</h1>
    </div>
    <div class="product-info">
      <p class="product-type">Organic Hair Oil</p>
      <p class="product-volume">100 ml</p>
    </div>
  </main>
</body>
</html>
```